Professional DJ Business Card

Business card for giving out to clubs and venues or interested groups that are in need of a professional DJ. I want something artistic and catchy/alluring, with a minimalist approach that gets just the vital amount of info and leaves the rest for inquiry via contacting me. Ideally I would like one side to have an image of something cool like an eye and my name, then the other side be the contact info, I am definitely feeling a black or dark colored card, but I am open to other designs. I am uploading a picture that I made that reflects a little of what I am *kind of* looking for.

Industry/Entity Type

Business

Contact Information for Business Card

Tomas Halvik (Voxtel)
Professional DJ (West Coast)
EDM (Deep/House/Techno), Hip Hop, Latin, Trap.
Cell: 555-274-9163
Email: Voxtelofficial@mailnest.net
www.beatcloudia.net/yourtuneisfading

```html
<!DOCTYPE html>
<html lang="en">
<head>
<meta charset="UTF-8">
<title>Voxtel – DJ Business Card</title>
<link href="https://fonts.googleapis.com/css2?family=Open+Sans:wght@400;600;700&display=swap" rel="stylesheet">
<style>
  :root {
    --backdrop: #e6e4e1;
    --card-dark: #0f1412;
    --card-dark-edge: #1b2220;
    --card-light: #ffffff;
    --ink-light: #f2f2f2;
    --ink-soft: #c9cccb;
    --divider: #6a706e;
    --art-dark: #2a302e;
    --art-light: #d8d8d8;
  }
  * { margin: 0; padding: 0; box-sizing: border-box; }
  html, body {
    width: 1200px; height: 843px; overflow: hidden;
    background: var(--backdrop);
    font-family: "Open Sans", Arial, sans-serif;
  }
  .canvas {
    position: relative; width: 1200px; height: 843px;
  }
  .card {
    position: absolute; left: 250px; width: 700px; height: 400px;
    border-radius: 4px;
    box-shadow: 0 6px 18px rgba(0,0,0,0.18);
    overflow: hidden;
  }
  .card--back { top: 14px; background: var(--card-light); }
  .card--front {
    top: 429px;
    background: linear-gradient(135deg, var(--card-dark-edge) 0%, var(--card-dark) 60%);
    color: var(--ink-light);
  }
  .back-eye-art {
    position: absolute; left: 250px; top: 130px; width: 200px; height: 110px;
    border-radius: 55px / 40px;
    background: radial-gradient(ellipse at center, #9a9a9a 0%, var(--art-light) 55%, var(--card-light) 100%);
  }
  .front-eye-art {
    position: absolute; left: 330px; top: 28px; width: 240px; height: 120px;
    border-radius: 60px / 45px;
    background: radial-gradient(ellipse at center, #8d9290 0%, var(--art-dark) 55%, transparent 100%);
  }
  .brand-name {
    position: absolute; left: 220px; top: 105px;
    font-size: 52px; font-weight: 700; color: var(--ink-light);
    letter-spacing: 1px;
  }
  .identity {
    position: absolute; left: 70px; top: 225px; width: 270px; text-align: right;
  }
  .identity__name { font-size: 21px; font-weight: 700; }
  .identity__role { font-size: 17px; font-weight: 400; color: var(--ink-soft); margin-top: 2px; }
  .divider {
    position: absolute; left: 360px; top: 225px; width: 1px; height: 140px;
    background: var(--divider);
  }
  .details { position: absolute; left: 380px; top: 222px; font-size: 16px; line-height: 1.3; }
  .details__genres { margin-bottom: 10px; }
  .details__row { display: flex; align-items: center; gap: 10px; margin-bottom: 6px; color: var(--ink-light); }
  .details__row svg { width: 16px; height: 16px; flex: none; }
</style>
</head>
<body>
<div class="canvas">
  <section class="card card--back">
    <div class="back-eye-art" role="img" aria-label="Sketched eye illustration with radiating lines"></div>
  </section>

  <section class="card card--front">
    <div class="front-eye-art" role="img" aria-label="Sketched eye illustration with radiating lines"></div>
    <div class="brand-name">Voxtel</div>

    <div class="identity">
      <div class="identity__name">Tomas Halvik (Voxtel)</div>
      <div class="identity__role">Professional DJ (West Coast)</div>
    </div>

    <div class="divider"></div>

    <div class="details">
      <div class="details__genres">EDM (Deep/House/Techno)<br>Hip Hop, Latin, Trap.</div>
      <div class="details__row">
        <svg viewBox="0 0 16 16" aria-hidden="true"><rect x="4" y="1" width="8" height="14" rx="1.5" fill="none" stroke="#f2f2f2" stroke-width="1.5"/><circle cx="8" cy="12.5" r="0.9" fill="#f2f2f2"/></svg>
        <span>555-274-9163</span>
      </div>
      <div class="details__row">
        <svg viewBox="0 0 16 16" aria-hidden="true"><rect x="1" y="3" width="14" height="10" fill="none" stroke="#f2f2f2" stroke-width="1.5"/><path d="M1 3 L8 9 L15 3" fill="none" stroke="#f2f2f2" stroke-width="1.5"/></svg>
        <span>Voxtelofficial@mailnest.net</span>
      </div>
      <div class="details__row">
        <svg viewBox="0 0 16 16" aria-hidden="true"><circle cx="8" cy="8" r="6" fill="#f2f2f2"/></svg>
        <span>yourtuneisfading</span>
      </div>
    </div>
  </section>
</div>
</body>
</html>
```